Holistic Health Coach needs a catchy and creative flyer

I need an eye-catching and convincing DL sized flyer for my new health coaching business. I provide advice and regular coaching to people on health, fitness and lifestyle issues.

I want these flyers to create awareness of my business as well as providing some information about what I do and the services that I can provide. I also want the flyers to have a strong and clear call-to-action so they can contact me.

I have provided some photos myself to be used in the flyer if necessary. I have also provided my logo. My Business name is called "Our Vital Ledger" however I want to market myself as a " Qualified Holistic Health Coach".

Target Market(s)

Men and Women of all ages who are trying to improve their health and fitness

Industry/Entity Type

Health And Wellness

Font styles to use
Sans Serif

Requirements
Must have
• My Business is called "Our Vital Ledger" (as seen in attached logo) but I would like the main marketing message of the flyer to be focused as " Qualified Holistic Health Coach" .
• The Flyer should be DL size.
• Strong call to action
• Catchy and memorable design- as I am a new business I want this to capture people's attention.
• Please see attached document for page content.
Nice to have
• I have also included some recent pictures of myself to be incorporated in the flyer, if appropriate.

```html
<!DOCTYPE html>
<html lang="en">
<head>
<meta charset="utf-8">
<title>Our Vital Ledger – Holistic Health Coach DL Flyer</title>
<link rel="stylesheet" href="https://fonts.googleapis.com/css2?family=Amatic+SC:wght@700&family=Lato:wght@400;700;900&display=swap">
<style>
  :root {
    --ink: #1d1d1d;
    --band: #1a1a1a;
    --green: #4f9a2a;
    --lime: #8cc63f;
    --tick: #d0312d;
    --paper-light: #eeeeee;
    --paper-mid: #d9d9d9;
    --stage: #e6e6e6;
    --white: #ffffff;
    --muted: #333333;
  }
  * { box-sizing: border-box; margin: 0; padding: 0; }
  html, body { width: 1200px; height: 1151px; overflow: hidden; }
  body { background: var(--stage); font-family: "Lato", sans-serif; color: var(--ink); position: relative; }

  .flyer {
    position: absolute; top: 80px; width: 470px; height: 990px; overflow: hidden;
    background: radial-gradient(ellipse at 40% 30%, var(--paper-light), var(--paper-mid));
  }
  .flyer--front { left: 90px; }
  .flyer--back { left: 640px; }

  .hand { font-family: "Amatic SC", sans-serif; font-weight: 700; color: var(--ink); text-transform: uppercase; }
  .accent { color: var(--green); }

  /* Front */
  .topic-bar {
    position: absolute; top: 0; left: 0; right: 0; height: 48px; background: var(--band);
    color: var(--white); font-weight: 900; font-size: 19px; letter-spacing: 3px;
    display: flex; align-items: center; justify-content: center; gap: 10px;
  }
  .topic-bar .lime { color: var(--lime); }
  .topic-bar .sep { font-weight: 400; opacity: .8; }

  .photo-food {
    position: absolute; top: 48px; left: 0; width: 165px; height: 640px;
    background: linear-gradient(180deg, #f2f2f2 0%, #b7d67a 25%, #d8c7a0 45%, #7fb844 62%, #cfd9d0 85%, #dcdcdc 100%);
  }
  .headline {
    position: absolute; top: 58px; left: 175px; width: 285px;
    font-size: 68px; line-height: 68px; text-align: center;
  }
  .photo-coach {
    position: absolute; top: 430px; left: 275px; width: 195px; height: 560px;
    background: linear-gradient(180deg, #d7d7d7 0%, #b08a6a 18%, #f7f7f7 45%, #f0f0f0 80%, #1f2b44 92%);
  }
  .coach-quote {
    position: absolute; top: 745px; left: 28px; width: 236px;
    font-size: 38px; line-height: 40px; text-align: center;
  }
  .signature { position: absolute; top: 880px; left: 28px; width: 236px; text-align: right; }
  .signature .name { font-weight: 900; font-size: 20px; }
  .signature .creds { font-size: 11px; line-height: 14px; margin-top: 4px; color: var(--muted); }

  /* Back */
  .photo-props {
    position: absolute; top: 0; right: 0; width: 125px; height: 260px;
    background: radial-gradient(ellipse at 55% 35%, #8cc63f 0%, #6aa92c 35%, #dfe7e0 70%, transparent 90%);
  }
  .focus-list { position: absolute; top: 36px; left: 38px; list-style: none; }
  .focus-list li {
    display: flex; align-items: center; gap: 12px; font-weight: 700; font-size: 20px; line-height: 30px;
  }
  .focus-list svg { width: 22px; height: 22px; flex: none; }

  .services { position: absolute; top: 205px; left: 80px; width: 340px; }
  .services h2 { color: var(--green); font-weight: 900; font-size: 19px; margin-bottom: 4px; }
  .services ul { list-style: none; }
  .services li { font-size: 14px; line-height: 20px; padding-left: 16px; position: relative; }
  .services li::before {
    content: ""; position: absolute; left: 2px; top: 8px; width: 5px; height: 5px;
    border-radius: 50%; background: var(--green);
  }

  .cta { position: absolute; top: 500px; left: 0; right: 0; text-align: center; font-size: 70px; }

  .contact { position: absolute; top: 630px; left: 0; right: 0; text-align: center; font-size: 19px; line-height: 32px; }
  .contact b { color: var(--green); font-weight: 900; }
  .contact .note { font-size: 13px; margin-top: 14px; line-height: 18px; }

  .footer {
    position: absolute; bottom: 0; left: 0; right: 0; height: 160px; background: var(--band);
    color: var(--white); display: flex; flex-direction: column; align-items: center; justify-content: center; gap: 14px;
  }
  .brand { display: flex; align-items: center; gap: 10px; font-weight: 900; font-size: 22px; letter-spacing: 1px; color: var(--lime); }
  .brand .dot { width: 26px; height: 26px; border-radius: 50%; background: var(--lime); }
  .footer .web { font-size: 19px; }
</style>
</head>
<body>
  <section class="flyer flyer--front">
    <div class="topic-bar">
      <span>Health</span><span class="sep">|</span><span class="lime">Nutrition</span><span class="sep">|</span><span>Lifestyle</span>
    </div>
    <div class="photo-food" role="img" aria-label="Healthy food, sneakers, tape measure, green apples and water bottle"></div>
    <h1 class="headline hand">"Be your<br>best through<br><span class="accent">food and<br>lifestyle</span><br>changes."</h1>
    <div class="photo-coach" role="img" aria-label="Portrait of the health coach in a white top, arms crossed"></div>
    <p class="coach-quote hand">"I can help, I'm a qualified holistic <span class="accent">health coach."</span></p>
    <div class="signature">
      <div class="name">— Clara Dunmore</div>
      <div class="creds">Bachelor in Sport &amp; Exercise,<br>Masters of Pharmacy</div>
    </div>
  </section>

  <section class="flyer flyer--back">
    <div class="photo-props" role="img" aria-label="Green apples and a water bottle"></div>
    <ul class="focus-list">
      <li><svg viewBox="0 0 22 22"><rect x="1" y="5" width="15" height="15" fill="none" stroke="#1d1d1d" stroke-width="1.6"/><path d="M4 12 l4 5 L20 2" fill="none" stroke="#d0312d" stroke-width="3" stroke-linecap="round"/></svg>Nutritional Advice</li>
      <li><svg viewBox="0 0 22 22"><rect x="1" y="5" width="15" height="15" fill="none" stroke="#1d1d1d" stroke-width="1.6"/><path d="M4 12 l4 5 L20 2" fill="none" stroke="#d0312d" stroke-width="3" stroke-linecap="round"/></svg>Fitness Planning</li>
      <li><svg viewBox="0 0 22 22"><rect x="1" y="5" width="15" height="15" fill="none" stroke="#1d1d1d" stroke-width="1.6"/><path d="M4 12 l4 5 L20 2" fill="none" stroke="#d0312d" stroke-width="3" stroke-linecap="round"/></svg>Natural Health Management</li>
      <li><svg viewBox="0 0 22 22"><rect x="1" y="5" width="15" height="15" fill="none" stroke="#1d1d1d" stroke-width="1.6"/><path d="M4 12 l4 5 L20 2" fill="none" stroke="#d0312d" stroke-width="3" stroke-linecap="round"/></svg>Lifestyle Enhancement</li>
    </ul>

    <div class="services">
      <h2>My services:</h2>
      <ul>
        <li>Weight Loss</li>
        <li>Reduce Medication Costs</li>
        <li>Nutritional Support</li>
        <li>Exercise Guidance</li>
        <li>Sleep Improvement</li>
        <li>Reducing Stress</li>
        <li>Improve Strength, Flexibility and Mobility</li>
        <li>Guidance on Vitamins and Supplements</li>
        <li>Practical Condition Management</li>
        <li>Food Tips and Education</li>
        <li>Realistic, Progressive, Tailored Advice</li>
      </ul>
    </div>

    <h2 class="cta hand">Get started now!</h2>

    <div class="contact">
      <p>Contact <b>Clara Dunmore</b></p>
      <p><b>Phone:</b> (02) 5550 1842</p>
      <p><b>Mobile:</b> 0400 555 218</p>
      <p><b>Email:</b> clara@ourvitalledger.com.au</p>
      <p class="note">Home consultations available.</p>
    </div>

    <footer class="footer">
      <div class="brand"><span class="dot"></span><span>OUR VITAL LEDGER</span></div>
      <div class="web">www.ourvitalledger.com.au</div>
    </footer>
  </section>
</body>
</html>
```